Business Card Design Project

Im an electrician and my company name is Kestrel Electrical
My main work is installing Lighting and Power Points, Home Theater Systems, TVS, Phones and Data
Im looking a business card, something nice, clean, modern and not to cluttered
Im open to sugestions
I dont mind if the "Services" is on the back on the business card
colours black, grey, white or the blue colour of my logo are prefered but not compulsory
any questions just message me
and please make it so if i need to edit the writing can do it easy. maybe by making it a seperate layer ?
My Details are.
Name - Peter Halloran
Job Title - Licenced Electrician
Mobile - 027 583 2174
Email - peter@kestrelelectrical.co.nz
Web - www.kestrelelectrical.co.nz
Services
Residential / Commercial
Lighting & Power
Heating & Ventilation
Automation
Phone & Data
Home Cinema
Sound Systems
TV, Antenna & Satellite
Digital Upgrades

```html
<!DOCTYPE html>
<html lang="en">
<head>
<meta charset="utf-8">
<title>Kestrel Electrical – Business Card</title>
<link rel="stylesheet" href="https://fonts.googleapis.com/css2?family=Exo+2:wght@600&family=Roboto+Condensed:wght@400;700&family=Questrial&display=swap">
<style>
  :root {
    --stage: #2b2b2b;
    --card-black: #111213;
    --card-cyan: #12b5d4;
    --stripe-grey: #8c8f93;
    --text-white: #f2f2f2;
    --text-grey: #a9adb2;
    --text-dark: #0d0d0d;
  }
  * { box-sizing: border-box; margin: 0; padding: 0; }
  html, body { width: 1200px; height: 900px; overflow: hidden; }
  body {
    background: var(--stage);
    display: flex;
    align-items: center;
    justify-content: center;
    gap: 40px;
  }
  .card {
    position: relative;
    width: 540px;
    height: 309px;
    overflow: hidden;
    background: var(--card-black);
    box-shadow: 0 14px 30px rgba(0,0,0,.45);
  }

  /* ---------- Front ---------- */
  .front__band {
    position: absolute;
    left: 0; right: 0; top: 150px; bottom: 0;
    background: var(--card-cyan);
  }
  .front__stripe {
    position: absolute;
    left: 0; right: 0; top: 136px;
    height: 8px;
    background: var(--stripe-grey);
  }
  .brand {
    position: absolute;
    display: flex;
    align-items: center;
    gap: 14px;
    font-family: "Exo 2", sans-serif;
    font-weight: 600;
    color: var(--text-white);
    letter-spacing: 2px;
    text-transform: uppercase;
  }
  .brand__square {
    background: var(--card-cyan);
    flex: none;
  }
  .front .brand { left: 36px; top: 44px; font-size: 30px; }
  .front .brand__square { width: 46px; height: 46px; }

  .person {
    position: absolute;
    left: 36px; top: 190px;
    font-family: "Roboto Condensed", sans-serif;
    color: var(--text-dark);
    text-transform: uppercase;
  }
  .person__name { font-size: 24px; font-weight: 700; line-height: 1; }
  .person__role { font-size: 11px; font-weight: 700; letter-spacing: .5px; margin-top: 4px; text-align: right; }

  .front__divider {
    position: absolute;
    left: 258px; top: 180px;
    width: 1px; height: 90px;
    background: rgba(0,0,0,.35);
  }
  .contact {
    position: absolute;
    left: 276px; top: 186px;
    list-style: none;
    font-family: "Roboto Condensed", sans-serif;
    font-size: 14px;
    color: var(--text-dark);
    text-transform: uppercase;
  }
  .contact li { display: flex; align-items: center; gap: 10px; height: 26px; }
  .contact svg { width: 13px; height: 13px; flex: none; }

  /* ---------- Back ---------- */
  .back__panel {
    position: absolute;
    left: 0; top: 0; bottom: 0;
    width: 150px;
    background: var(--card-cyan);
  }
  .back .brand { left: 190px; top: 44px; font-size: 28px; }
  .services {
    position: absolute;
    left: 190px; top: 130px;
    width: 320px;
    list-style: none;
    display: grid;
    grid-template-columns: 1fr 1fr;
    row-gap: 4px;
    column-gap: 10px;
    font-family: "Questrial", sans-serif;
    font-size: 12.5px;
    color: var(--text-grey);
  }
  .services li::before { content: "- "; }
  .back__web {
    position: absolute;
    right: 30px; bottom: 30px;
    font-family: "Questrial", sans-serif;
    font-size: 16px;
    color: var(--card-cyan);
    letter-spacing: .3px;
  }
</style>
</head>
<body>

  <section class="card front" aria-label="Business card front">
    <div class="front__stripe"></div>
    <div class="front__band"></div>

    <div class="brand">
      <span class="brand__square"></span>
      <span class="brand__name">Kestrel Electrical</span>
    </div>

    <div class="person">
      <p class="person__name">Peter Halloran</p>
      <p class="person__role">Licenced Electrician</p>
    </div>

    <div class="front__divider"></div>

    <ul class="contact">
      <li>
        <svg viewBox="0 0 16 16" aria-hidden="true"><path fill="#0d0d0d" d="M3.6 1.2l2.2 2.6-1.3 1.8c.9 2 2.4 3.5 4.4 4.4l1.8-1.3 2.6 2.2-1.2 2.6C6.5 14.8 1.2 9.5.9 3z"/></svg>
        <span>027 583 2174</span>
      </li>
      <li>
        <svg viewBox="0 0 16 16" aria-hidden="true"><rect x="1" y="3" width="14" height="10" fill="none" stroke="#0d0d0d" stroke-width="1.6"/><path d="M1 3.5l7 5 7-5" fill="none" stroke="#0d0d0d" stroke-width="1.6"/></svg>
        <span>peter@kestrelelectrical.co.nz</span>
      </li>
      <li>
        <svg viewBox="0 0 16 16" aria-hidden="true"><g fill="none" stroke="#0d0d0d" stroke-width="1.4"><circle cx="8" cy="8" r="6.5"/><ellipse cx="8" cy="8" rx="2.8" ry="6.5"/><path d="M1.5 8h13"/></g></svg>
        <span>www.kestrelelectrical.co.nz</span>
      </li>
    </ul>
  </section>

  <section class="card back" aria-label="Business card back">
    <div class="back__panel"></div>

    <div class="brand">
      <span class="brand__name">Kestrel Electrical</span>
    </div>

    <ul class="services">
      <li>Residential / Commercial</li>
      <li>Lighting &amp; Power</li>
      <li>Heating &amp; Ventilation</li>
      <li>Automation</li>
      <li>Phone &amp; Data</li>
      <li>Home Cinema</li>
      <li>Sound Systems</li>
      <li>TV, Antenna &amp; Satellite</li>
      <li>Digital Upgrades</li>
    </ul>

    <p class="back__web">www.kestrelelectrical.co.nz</p>
  </section>

</body>
</html>
```